I need a business card representing my company, VELDRA, it's an artist management and design company. Complete name is "VELDRA Artist Mgmt. + Design Co." I need it to be world class and very appealing, sophisticated and artistically unique.
Updates

Posted an updated Brief please see. I need a business card representing my company, VELDRA, it's an artist management and design company. Complete name is "VELDRA Artist Mgmt. + Design Co." I need it to be world class and very appealing, sophisticated and artistically unique.

Designs look the same

Designs look the same

Target Market(s)

Advertisers, Entertainment Companies, Commercial companies

Industry/Entity Type

Advertising

Contact Information for Business Card

I need a business card representing my company, VELDRA, it's an artist management and design company. Complete name is "VELDRA Artist Mgmt. + Design Co." I need it to be world class and very appealing, sophisticated and artistically unique. One side can be VELDRA Artist Mgmt. + Design Co. and the other my name, Teodoro Lindqvist, my contact telephone: 412.638.2957, email veldraartist@plumora.net, my address: 3264 Harwell Ave. #517 Miami, FL 33184

Font styles to use
Other font styles liked:
• Calibri

Colors
ffffff
0455a3
f37122

Requirements
Must have
• "VELDRA" stand out bigger than the rest of the text.
Nice to have
• Name "VELDRA" can be centered on one side or in the corner or along side edges, just need something cool and different.
Should not have
• I am open just try to keep it clean looking

```html
<!DOCTYPE html>
<html lang="en">
<head>
<meta charset="utf-8">
<title>VELDRA Artist Mgmt. + Design Co. — Business Card</title>
<link rel="stylesheet" href="https://fonts.googleapis.com/css2?family=PT+Sans+Narrow:wght@700&family=Tinos:wght@400;700&display=swap">
<style>
  :root {
    --backdrop: #8b8b8e;
    --card: #9b5557;
    --card-fold: #8a4a4c;
    --card-light: #a9625f;
    --tag: #dcdcdc;
    --tag-shade: #b9b9b9;
    --ink: #161211;
    --olive: #a8a045;
    --orange: #e8892f;
  }
  * { box-sizing: border-box; margin: 0; padding: 0; }
  html, body { width: 1200px; height: 686px; overflow: hidden; }
  body {
    background: var(--backdrop);
    position: relative;
    font-family: "Tinos", "Times New Roman", serif;
    color: var(--ink);
  }
  .card {
    position: absolute;
    top: 190px;
    width: 530px;
    height: 303px;
    background: var(--card);
    overflow: hidden;
  }
  .card--back { left: 45px; }
  .card--front { left: 625px; }
  .card__folds { position: absolute; inset: 0; }

  /* back side */
  .contact-list {
    position: absolute;
    top: 34px;
    right: 44px;
    list-style: none;
    font-size: 17px;
    line-height: 34px;
  }
  .contact-list li { display: flex; align-items: center; gap: 16px; }
  .contact-list svg { width: 18px; height: 18px; fill: var(--ink); }
  .person {
    position: absolute;
    left: 40px;
    bottom: 44px;
    display: flex;
    align-items: center;
    gap: 16px;
  }
  .marker { width: 34px; height: 34px; }
  .marker--orange { background: var(--orange); }
  .marker--olive { background: var(--olive); }
  .person__name {
    font-weight: 700;
    font-size: 17px;
    letter-spacing: 0.04em;
    text-transform: uppercase;
  }
  .person__email { font-size: 16px; }

  /* front side */
  .tag {
    position: absolute;
    background: var(--tag);
    box-shadow: 3px 3px 0 var(--tag-shade);
    font-size: 16px;
    letter-spacing: 0.04em;
    padding: 9px 18px;
    white-space: nowrap;
    transform-origin: left top;
  }
  .tag--design { left: 38px; top: 40px; transform: rotate(-18deg); }
  .tag--mgmt { left: 70px; top: 96px; transform: rotate(-18deg); }
  .brand {
    position: absolute;
    right: 40px;
    bottom: 40px;
    text-align: right;
  }
  .brand__row { display: flex; align-items: center; gap: 14px; justify-content: flex-end; }
  .brand__name {
    font-family: "PT Sans Narrow", "Arial Narrow", sans-serif;
    font-weight: 700;
    font-size: 64px;
    line-height: 1;
    letter-spacing: 0.02em;
  }
  .brand__web { font-size: 16px; margin-top: 6px; }
</style>
</head>
<body>

<section class="card card--back" aria-label="Business card, contact side">
  <svg class="card__folds" viewBox="0 0 530 303" aria-hidden="true">
    <polygon points="0,130 300,0 530,0 530,60 0,150" fill="var(--card-light)" opacity="0.35"/>
    <line x1="0" y1="150" x2="530" y2="60" stroke="var(--card-fold)" stroke-width="2"/>
  </svg>
  <ul class="contact-list">
    <li>
      <svg viewBox="0 0 24 24"><path d="M6.6 10.8a15 15 0 0 0 6.6 6.6l2.2-2.2c.3-.3.7-.4 1-.2 1.1.4 2.3.6 3.6.6.6 0 1 .4 1 1V20c0 .6-.4 1-1 1A17 17 0 0 1 3 4c0-.6.4-1 1-1h3.5c.6 0 1 .4 1 1 0 1.3.2 2.5.6 3.6.1.3 0 .7-.2 1z"/></svg>
      +412 638 2957
    </li>
    <li>
      <svg viewBox="0 0 24 24"><path d="M7 2h8v5H7zM4 8h16v12H4zm3 3v2h4v-2zm6 0v2h4v-2zm-6 4v2h4v-2zm6 0v2h4v-2z"/></svg>
      +412 638 5170
    </li>
    <li>
      <svg viewBox="0 0 24 24"><path d="M8 1h8a2 2 0 0 1 2 2v18a2 2 0 0 1-2 2H8a2 2 0 0 1-2-2V3a2 2 0 0 1 2-2zm0 3v14h8V4zm4 15.5a1 1 0 1 0 0 2 1 1 0 0 0 0-2z"/></svg>
      +412 638 7743
    </li>
  </ul>
  <div class="person">
    <div class="marker marker--orange"></div>
    <div>
      <p class="person__name">Teodoro Lindqvist</p>
      <p class="person__email">tlindqvist@veldraart.net</p>
    </div>
  </div>
</section>

<section class="card card--front" aria-label="Business card, brand side">
  <svg class="card__folds" viewBox="0 0 530 303" aria-hidden="true">
    <polygon points="0,0 330,0 0,120" fill="var(--card-light)" opacity="0.35"/>
    <line x1="0" y1="120" x2="330" y2="0" stroke="var(--card-fold)" stroke-width="2"/>
    <line x1="0" y1="175" x2="480" y2="0" stroke="var(--card-fold)" stroke-width="2"/>
  </svg>
  <div class="tag tag--design">DESIGN CO</div>
  <div class="tag tag--mgmt">ARTIST MANAGEMENT</div>
  <div class="brand">
    <div class="brand__row">
      <div class="marker marker--olive"></div>
      <p class="brand__name">VELDRA</p>
    </div>
    <p class="brand__web">www.veldraart.net</p>
  </div>
</section>

</body>
</html>
```